Velora aesthetics offers a range of facial aesthetics treatments by a fully qualified dentist, to a high end crowd. Treatments include antiwrinkle treatment, the use of dermal fillers to provide facial volumisation and rejuvenation and also lip volumisation.
I want a luxurious and bold look. Black background with a bold striking gold logo in the centre possibly incorporating the outline of a face in a subtle yet effective way. I want it to include the work I offer so people will be aware of what they are looking into but not look like there's too much on the card, So it's a clean look.
At the bottom I would like it to say by Dr. Anjali Desai. Alongside my email address and mobile number.

```html
<!DOCTYPE html>
<html lang="en">
<head>
<meta charset="utf-8">
<title>Velora aesthetics – Business Card</title>
<link href="https://fonts.googleapis.com/css2?family=Questrial&family=Roboto:wght@400;500&display=swap" rel="stylesheet">
<style>
  :root {
    --backdrop: #1d1d1f;
    --card: #262626;
    --gold: #f2b705;
    --gold-soft: #c9950a;
    --ink: #e8e8e8;
    --rule: #5a5a5a;
  }
  html, body {
    margin: 0;
    width: 1200px;
    height: 798px;
    overflow: hidden;
    background: var(--backdrop);
  }
  .canvas {
    position: relative;
    width: 1200px;
    height: 798px;
  }
  .card {
    position: absolute;
    left: 240px;
    top: 194px;
    width: 720px;
    height: 410px;
    background: var(--card);
    box-sizing: border-box;
    font-family: "Roboto", sans-serif;
    color: var(--ink);
  }
  .brand {
    position: absolute;
    left: 0;
    right: 0;
    top: 78px;
    display: flex;
    align-items: center;
    justify-content: center;
    gap: 18px;
  }
  .brand-dot {
    width: 46px;
    height: 46px;
    border-radius: 50%;
    background: var(--gold);
  }
  .brand-name {
    font-family: "Questrial", sans-serif;
    font-size: 34px;
    color: var(--gold);
    letter-spacing: 0.5px;
  }
  .brand-rule {
    position: absolute;
    left: 300px;
    right: 40px;
    top: 160px;
    height: 1px;
    background: var(--rule);
  }
  .services {
    position: absolute;
    left: 0;
    right: 0;
    top: 186px;
    margin: 0;
    padding: 0;
    list-style: none;
    text-align: center;
    font-size: 16px;
    line-height: 22px;
  }
  .footer {
    position: absolute;
    left: 40px;
    right: 40px;
    bottom: 38px;
    display: flex;
    align-items: center;
    gap: 26px;
    font-size: 14px;
    line-height: 20px;
  }
  .footer-rule {
    position: absolute;
    left: 40px;
    right: 40px;
    bottom: 100px;
    height: 1px;
    background: var(--rule);
  }
  .person-name {
    font-weight: 500;
    font-size: 17px;
  }
  .person-role {
    color: var(--gold);
  }
  .divider {
    width: 1px;
    height: 32px;
    background: var(--gold-soft);
  }
  .contact-line {
    display: flex;
    align-items: center;
    gap: 8px;
  }
  .contact-line svg {
    width: 12px;
    height: 12px;
    fill: var(--gold);
  }
</style>
</head>
<body>
<div class="canvas">
  <div class="card">
    <div class="brand">
      <span class="brand-dot"></span>
      <span class="brand-name">Velora aesthetics</span>
    </div>
    <div class="brand-rule"></div>

    <ul class="services">
      <li>Antiwrinkle treatment</li>
      <li>Dermal fillers to provide facial volumisation rejuvenation</li>
      <li>Lip volumisation</li>
    </ul>

    <div class="footer-rule"></div>
    <div class="footer">
      <div class="person">
        <div class="person-name">Dr. Anjali Desai.</div>
        <div class="person-role">Dentist</div>
      </div>
      <span class="divider"></span>
      <address class="address" style="font-style:normal">
        2210 Harbor Lane Suite 410<br>
        Millbrook, Il 60422
      </address>
      <span class="divider"></span>
      <div class="contact">
        <div class="contact-line">
          <svg viewBox="0 0 24 24" aria-hidden="true"><path d="M6.6 10.8a15.1 15.1 0 0 0 6.6 6.6l2.2-2.2c.3-.3.7-.4 1-.2 1.1.4 2.3.6 3.6.6.6 0 1 .4 1 1V20c0 .6-.4 1-1 1A17 17 0 0 1 3 4c0-.6.4-1 1-1h3.5c.6 0 1 .4 1 1 0 1.3.2 2.5.6 3.6.1.3 0 .7-.2 1z"/></svg>
          <span>0745-219-530</span>
        </div>
        <div class="contact-line">
          <svg viewBox="0 0 24 24" aria-hidden="true"><path d="M2 5h20v14H2z M2 5l10 8 10-8" /></svg>
          <span>Anjali@Desai.com</span>
        </div>
      </div>
    </div>
  </div>
</div>
</body>
</html>
```